Family Business Father/Son Consulting team needs a cover for their book on family workplace dynamics

We are a father/son consulting firm that focuses on the psychology of communication and performance in the workplace of financial advisors. We recently wrote a book on the topic of family members working in the same financial services practice together. So, we need someone to design the cover for our book. The book itself is in a self-help style with the occasional exercise. It is psychologically based and while specific to the finance industry, does not discuss finances itself.

We would like the cover to clearly communicate that this book is practical, easy to read, and impactful. The average reader is someone who is successful in business and work or will soon plan on working with a family member.

The Title is "The Steady Kinship Crew: Shaping, Growing, and Handing Over a Household Enterprise in Wealth Advising" by Owen Pelkart, FDC*TM(this should be a trademark) and Rob Pelkart, Ph.D. Foreword by Joan Merrow.

Target Market(s)

Financial advisors who work with family members. Usually it is a parent/child, but not always.

Industry/Entity Type

Consulting within Financial Services

Colors

Designer to choose colors to be used in the design.

Requirements
Must have
• The ability for the design to be a printed book and for E-book
Nice to have
• Could be a simple design with the title or with graphics,. We are open to either. Our business colors are in the royal blue range. So, that color scheme could be nice, but isn't essential if there is something more creative/better that you have in mind.
Should not have
• Extravagant/ too playful of colors, but can be fun with design

```html
<!DOCTYPE html>
<html lang="en">
<head>
<meta charset="utf-8">
<title>The Steady Kinship Crew — Book Cover</title>
<link rel="stylesheet" href="https://fonts.googleapis.com/css2?family=Cinzel:wght@400;600&family=Sorts+Mill+Goudy&display=swap">
<style>
  :root {
    --sky-top: #c9ad7a;
    --sky-sand: #dcc6a0;
    --sky-cream: #efe4cf;
    --sky-mist: #d8cdbb;
    --sky-gold: #f3c866;
    --sky-amber: #eab050;
    --sea-teal: #2a7fa6;
    --sea-blue: #1d5f8c;
    --sea-deep: #123f69;
    --band-cream: #f4e8c9;
    --band-gold: #f3d98e;
    --ink-teal: #1c5670;
    --title-cream: #f4efd6;
    --author-cream: #eee3c6;
  }
  * { margin: 0; padding: 0; box-sizing: border-box; }
  html, body { width: 800px; height: 1200px; overflow: hidden; background: var(--sea-deep); }
  .cover {
    position: relative;
    width: 800px;
    height: 1200px;
    overflow: hidden;
  }
  .cover-art {
    position: absolute;
    inset: 0;
    background:
      radial-gradient(ellipse 220px 170px at 620px 260px, rgba(255,255,255,0.55), transparent 70%),
      radial-gradient(ellipse 320px 50px at 400px 655px, rgba(250,225,150,0.8), transparent 75%),
      linear-gradient(to bottom,
        var(--sky-top) 0px,
        var(--sky-sand) 70px,
        var(--sky-cream) 230px,
        var(--sky-cream) 440px,
        var(--sky-mist) 540px,
        var(--sky-gold) 620px,
        var(--sky-amber) 680px,
        var(--sea-blue) 705px,
        var(--sea-teal) 780px,
        var(--sea-blue) 860px,
        var(--sea-teal) 930px,
        var(--sea-blue) 1000px,
        var(--sea-deep) 1200px);
  }
  .family-figures {
    position: absolute;
    left: 10px;
    top: 235px;
    width: 720px;
    height: 470px;
    background: radial-gradient(ellipse 330px 260px at 50% 70%, rgba(29,95,140,0.28), rgba(29,95,140,0) 75%);
  }
  .foreword {
    position: absolute;
    top: 42px;
    left: 0;
    width: 800px;
    text-align: center;
    font-family: "Sorts Mill Goudy", Georgia, serif;
    font-size: 31px;
    color: var(--ink-teal);
    letter-spacing: 0.5px;
  }
  .title {
    position: absolute;
    top: 722px;
    left: 0;
    width: 800px;
    text-align: center;
    font-family: "Cinzel", "Times New Roman", serif;
    font-weight: 400;
    font-size: 92px;
    line-height: 106px;
    color: var(--title-cream);
    text-shadow: 2px 3px 4px rgba(10,30,50,0.55);
  }
  .subtitle-band {
    position: absolute;
    top: 960px;
    left: 0;
    width: 800px;
    height: 115px;
    background: linear-gradient(to right, var(--band-cream) 0%, #f2e6c6 55%, var(--band-gold) 100%);
    display: flex;
    align-items: center;
    justify-content: center;
  }
  .subtitle {
    font-family: "Sorts Mill Goudy", Georgia, serif;
    font-size: 31px;
    line-height: 39px;
    color: var(--ink-teal);
    text-align: center;
  }
  .authors {
    position: absolute;
    top: 1108px;
    left: 0;
    width: 800px;
    text-align: center;
    font-family: "Cinzel", "Times New Roman", serif;
    font-weight: 600;
    font-size: 27px;
    color: var(--author-cream);
    letter-spacing: 0.3px;
  }
  .authors sup { font-size: 14px; vertical-align: 12px; }
</style>
</head>
<body>
  <main class="cover">
    <div class="cover-art" role="img" aria-label="Painted sky in cream and gold over a blue sea at sunset"></div>
    <div class="family-figures" role="img" aria-label="Blue silhouettes of a father, mother and two children holding hands walking along a shore beside a flowering plant"></div>

    <p class="foreword">Foreword by Joan Merrow</p>

    <h1 class="title">THE STEADY<br>KINSHIP CREW</h1>

    <div class="subtitle-band">
      <p class="subtitle">Shaping, Growing, and Handing Over a<br>Household Enterprise in Wealth Advising</p>
    </div>

    <p class="authors">OWEN PELKART, FDC<sup>TM</sup> &amp; ROB PELKART, PH.D.</p>
  </main>
</body>
</html>
```